HARBORLINE AUTO GLASS

Mobile Glass Shop:

1) Windshield REPAIR 2)Windshield replacment 3) Rear Windshield Replacment 4) Side Window Replacment 5) car window replacment 6) Power Window Repair.

Schedual a service within 24 hour with one of our certified technicians.

See "brightvane auto repair" web site for referance on the nature of our buisness and service. www.brightvane-example.com

```html
<!DOCTYPE html>
<html lang="en">
<head>
<meta charset="utf-8">
<title>Harborline Auto Glass</title>
<link href="https://fonts.googleapis.com/css2?family=Oswald:wght@500;600&family=Open+Sans:ital,wght@0,400;0,600;1,400&display=swap" rel="stylesheet">
<style>
:root{
  --blue:#2b7bbd; --blue-dark:#1d4f7c; --navy:#132a44; --ink:#111418;
  --soft:#f4f5f8; --muted:#7b828c; --white:#fff; --black:#0d0d0d;
}
*{margin:0;padding:0;box-sizing:border-box}
html,body{width:1200px;height:1200px;overflow:hidden;background:#fff}
.stage{position:absolute;left:0;top:0;width:1932px;height:1932px;transform:scale(.62112);transform-origin:0 0}
.page{position:absolute;left:706px;top:0;width:520px;height:1932px;background:#fff;font-family:"Open Sans",sans-serif;color:var(--ink)}
.page *{position:absolute}
.h{font-family:"Oswald",sans-serif;font-weight:600;text-transform:uppercase;line-height:1.12}
.label{font-family:"Open Sans",sans-serif;font-weight:600;font-size:5.5px;letter-spacing:1.3px;color:var(--blue);text-transform:uppercase;white-space:nowrap}
.p{font-size:4.6px;line-height:1.8;color:var(--muted)}
.rule{height:1px;width:52px;background:var(--blue)}
.btn{height:14px;padding:0 9px;background:var(--blue);color:#fff;font-family:"Oswald",sans-serif;font-size:5px;line-height:14px;text-transform:uppercase;white-space:nowrap;clip-path:polygon(4% 0,100% 0,96% 100%,0 100%)}
.topbar{left:0;top:0;width:520px;height:12px;background:var(--blue);color:#fff;font-size:4px;line-height:12px}
.topbar span{white-space:nowrap}
.nav a{position:absolute;top:28px;font-family:"Oswald",sans-serif;font-size:5px;color:var(--ink);text-transform:uppercase;white-space:nowrap;text-decoration:none}
.logo{font-family:"Oswald",sans-serif;font-weight:600;color:var(--blue);font-size:9px;line-height:1;white-space:nowrap}
.offer-card{width:85px;height:85px;background:var(--soft);border:1px solid #e4e7ec}
.offer-card svg{left:28px;top:12px}
.offer-card .h{left:0;width:100%;top:46px;text-align:center;font-size:9px}
.svc{width:110px;height:132px;background:var(--blue-dark)}
.svc .photo{left:0;top:0;width:110px;height:80px}
.svc .box{left:6px;top:79px;width:99px;height:53px;background:#fff;text-align:center}
.svc .box svg{left:38px;top:10px}
.svc .box .h{left:0;width:100%;top:33px;font-size:6.3px}
.news{width:110px;height:147px;background:#fff}
.news .photo{left:0;top:0;width:110px;height:79px}
.news .date{left:84px;top:64px;width:22px;height:22px;background:var(--blue);color:#fff;text-align:center;font-family:"Oswald",sans-serif;font-size:9px;line-height:1.2;padding-top:2px}
.news .date small{position:static;display:block;font-size:3.5px;opacity:.8}
.news .h{left:8px;top:93px;width:96px;font-size:7px}
.news .p{left:8px;top:118px;width:96px;font-size:4px}
.foot h4{font-family:"Oswald",sans-serif;font-weight:600;font-size:7px;color:#fff;text-transform:uppercase;white-space:nowrap}
.foot ul{left:0;top:0;width:100%;height:100%;list-style:none}
.foot li{list-style:none;font-size:4.3px;line-height:1;color:#e6e6e6;white-space:nowrap}
.foot .small{font-size:4px;color:#bbb;white-space:nowrap}
</style>
</head>
<body>
<div class="stage">
<div class="page">

  <div class="topbar">
    <span style="left:86px">NEED ANY HELP CONTACT US</span>
    <svg style="left:149px;top:2px" width="8" height="8" viewBox="0 0 8 8"><circle cx="4" cy="4" r="4" fill="#fff"/><path d="M2.6 2.2l1 1-.5.6a3 3 0 0 0 1.1 1.1l.6-.5 1 1-.6.6c-1.6-.3-2.9-1.6-3.2-3.2z" fill="#2b7bbd"/></svg>
    <span style="left:159px;font-weight:600">+000 555 0142</span>
    <svg style="left:367px;top:3px" width="5" height="7" viewBox="0 0 5 7"><path d="M2.5 0A2.5 2.5 0 0 0 0 2.5C0 4.3 2.5 7 2.5 7S5 4.3 5 2.5A2.5 2.5 0 0 0 2.5 0z" fill="#fff"/><circle cx="2.5" cy="2.5" r="1" fill="#2b7bbd"/></svg>
    <span style="left:374px">48 QUAYSIDE ROAD, PORTVIEW</span>
  </div>

  <div class="nav" style="left:0;top:12px;width:520px;height:38px">
    <div style="left:86px;top:7px;width:16px;height:22px;background:var(--blue)"></div>
    <div class="logo" style="left:105px;top:11px;font-size:8px">HARBORLINE</div>
    <div class="logo" style="left:105px;top:21px;font-size:3.6px;letter-spacing:1.4px">AUTO GLASS</div>
    <a style="left:216px;top:16px">Home</a>
    <a style="left:241px;top:16px">Services</a>
    <a style="left:273px;top:16px">About Us</a>
    <a style="left:307px;top:16px">Locations</a>
    <a style="left:342px;top:16px">Contact Us</a>
    <div class="btn" style="left:382px;top:13px;width:53px;text-align:center;padding:0">Schedule Now</div>
  </div>

  <section style="left:1px;top:50px;width:518px;height:237px;background:linear-gradient(90deg,#14202e 0%,#1b4a74 45%,#2b7bbd 100%)">
    <div class="label" style="left:84px;top:47px;color:#3b8fd6">Service within 24 hour</div>
    <h1 class="h" style="left:83px;top:57px;width:180px;font-size:23px;color:#fff;line-height:1.1">Harborline Auto<br>Glass Repairing<br>Company</h1>
    <div class="rule" style="left:84px;top:140px;width:46px"></div>
    <p style="left:84px;top:146px;width:150px;font-size:5.5px;line-height:1.75;color:#fff">Schedule a service within 24 hour with one of our certified technicians.</p>
    <div class="btn" style="left:85px;top:174px">Our Services »</div>
    <div style="left:148px;top:174px;height:14px;padding:0 9px;border:1px solid #fff;color:#fff;font-family:Oswald,sans-serif;font-size:5px;line-height:12px;text-transform:uppercase;white-space:nowrap">Learn More »</div>
    <div role="img" aria-label="Technician fitting a new windshield onto a car" style="left:268px;top:22px;width:166px;height:194px;background:linear-gradient(160deg,#5b7fa4,#1f3a5a 70%,#2a4f76);clip-path:polygon(14% 0,80% 4%,100% 30%,92% 100%,0 94%,10% 50%)"></div>
  </section>

  <div class="offer-card" style="left:84px;top:318px">
    <svg width="28" height="28" viewBox="0 0 28 28" fill="none" stroke="#2b7bbd" stroke-width="1.2"><rect x="7" y="4" width="15" height="20" rx="1"/><path d="M4 8h3M4 8v18h14v-2M10 10h9M10 14h9M10 18h6"/></svg>
    <div class="h">Stress-Free<br>Claims</div>
  </div>
  <div class="offer-card" style="left:177px;top:327px">
    <svg width="28" height="28" viewBox="0 0 28 28" fill="none" stroke="#2b7bbd" stroke-width="1.2"><path d="M14 3a7 7 0 0 0-7 7c0 5 7 12 7 12s7-7 7-12a7 7 0 0 0-7-7z"/><circle cx="14" cy="10" r="2.5"/><path d="M6 20l-3 5h22l-3-5"/></svg>
    <div class="h">Shops Near<br>You</div>
  </div>
  <div class="offer-card" style="left:84px;top:410px">
    <svg width="28" height="28" viewBox="0 0 28 28" fill="none" stroke="#2b7bbd" stroke-width="1.2"><path d="M5 23L18 10M18 10a4 4 0 1 0 4-6l-3 3-2-2 3-3a4 4 0 0 0-5 5M7 5l16 16M7 5L4 8l3 3 3-3"/></svg>
    <div class="h">Superior<br>Repairs</div>
  </div>
  <div class="offer-card" style="left:177px;top:419px">
    <svg width="28" height="28" viewBox="0 0 28 28" fill="none" stroke="#2b7bbd" stroke-width="1.2"><circle cx="14" cy="7" r="3"/><path d="M9 18a5 5 0 0 1 10 0M3 12l3 10h16l3-10"/><circle cx="6" cy="10" r="1.5"/><circle cx="22" cy="10" r="1.5"/></svg>
    <div class="h">Customer<br>Support</div>
  </div>
  <div class="label" style="left:284px;top:344px">What we offer</div>
  <h2 class="h" style="left:284px;top:354px;width:160px;font-size:16.5px">The Best Choice For<br>Auto Glass Repair</h2>
  <div class="rule" style="left:284px;top:396px"></div>
  <p class="p" style="left:284px;top:403px;width:152px">Lorem ipsum dolor sit amet, consectetur adipiscing elit, sed do eiusmod tempor incididunt ut labore et dolore magna aliqua. Ut enim ad minim veniam, quis nostrud exercitation.</p>
  <p class="p" style="left:284px;top:433px;width:152px">Duis aute irure dolor in reprehenderit in voluptate velit esse cil lum dolore eu fugiat nulla pariatur. Excepteur sint ocaecat cupidat at non proident, sunt in culpa qui officia deserunt.</p>
  <div class="btn" style="left:285px;top:469px">Learn More »</div>

  <section style="left:0;top:533px;width:520px;height:244px;background:var(--soft)">
    <div class="label" style="left:85px;top:35px">About Harborline</div>
    <h2 class="h" style="left:85px;top:46px;width:175px;font-size:15.5px">About Harborline Auto<br>Glass Repair Company<br>Histories</h2>
    <p class="p" style="left:85px;top:116px;width:146px">Duis aute irure dolor in reprehenderit in voluptate velit esse cil lum dolore eu fugiat pariatur. Excepteur sint ocaecat cupidat at non proident, sunt in culpa qui officia deserunt.</p>
    <svg style="left:85px;top:150px" width="24" height="24" viewBox="0 0 24 24" fill="none" stroke="#2b7bbd" stroke-width="1"><circle cx="14" cy="9" r="4"/><circle cx="14" cy="9" r="6.5" stroke-dasharray="2 1.5"/><path d="M2 18h5l4 2h6l5-4M2 22h4"/></svg>
    <div class="h" style="left:117px;top:150px;font-size:6.2px;white-space:nowrap">Experience &amp; Professional</div>
    <p class="p" style="left:117px;top:159px;width:112px;font-size:4.3px">Sed ut perspiciatis unde omnis te natus error sit volupt accusatium doloremque laudantium.</p>
    <div class="btn" style="left:86px;top:187px">Learn More »</div>
    <div style="left:265px;top:150px;width:53px;height:51px;background:var(--blue);clip-path:polygon(0 0,16% 12%,16% 88%,100% 88%,100% 100%,0 100%)"></div>
    <div role="img" aria-label="Technician working on a car windshield" style="left:273px;top:53px;width:136px;height:140px;background:linear-gradient(150deg,#7d8a98,#2e3d4f 60%,#3c5168)"></div>
    <div role="img" aria-label="Close-up of glass being fitted to a car" style="left:367px;top:30px;width:67px;height:67px;background:linear-gradient(140deg,#a9b4c0,#4a5a6c);box-shadow:0 0 6px rgba(0,0,0,.15)"></div>
  </section>

  <section style="left:1px;top:777px;width:518px;height:416px;background:linear-gradient(120deg,#2b7bbd 0%,#1c4f80 40%,#11243a 75%,#0a0c10 100%)">
    <div class="label" style="left:0;width:518px;text-align:center;top:29px;color:#4b95d6">Our services</div>
    <h2 class="h" style="left:0;width:518px;text-align:center;top:39px;font-size:15.5px;color:#fff">We Provide Professional Auto<br>Glass Repair Services</h2>
    <div class="rule" style="left:233px;top:82px;background:#4b95d6"></div>
  </section>
  <div class="svc" style="left:85px;top:876px">
    <div class="photo" role="img" aria-label="Windshield crack being repaired" style="background:linear-gradient(150deg,#8fb0cf,#2f5674)"></div>
    <div class="box"><svg width="24" height="16" viewBox="0 0 24 16" fill="none" stroke="#2b7bbd" stroke-width="1"><path d="M2 4l20-3-2 13H4z"/><path d="M14 5l-2 3"/></svg><div class="h">Windshield Repair</div></div>
  </div>
  <div class="svc" style="left:205px;top:876px">
    <div class="photo" role="img" aria-label="Cracked windshield on a parked car" style="height:66px;background:linear-gradient(150deg,#b59a5a,#5b6f7d)"></div>
    <div class="box" style="left:5px;top:65px;width:100px;height:67px;background:var(--blue);color:#fff">
      <svg width="24" height="16" viewBox="0 0 24 16" fill="none" stroke="#fff" stroke-width="1"><path d="M2 5q10-6 20 0l-2 9H4z"/></svg>
      <div class="h" style="top:31px">Windshield Replacment</div>
      <p style="left:8px;top:42px;width:84px;font-size:3.7px;line-height:1.7;color:#e4eef8">Sed ut perspiciatis unde omnis te natus error sit volupt accusatium.</p>
    </div>
  </div>
  <div class="svc" style="left:325px;top:876px">
    <div class="photo" role="img" aria-label="Car interior seen through the rear window" style="background:linear-gradient(150deg,#c7c3c0,#6e4d4a)"></div>
    <div class="box"><svg width="24" height="16" viewBox="0 0 24 16" fill="none" stroke="#2b7bbd" stroke-width="1"><rect x="3" y="2" width="18" height="10"/><path d="M9 8l4 5"/></svg><div class="h" style="top:28px;line-height:1.35">Rear Windshield<br>Replacment</div></div>
  </div>
  <div class="svc" style="left:85px;top:1027px">
    <div class="photo" role="img" aria-label="Car door with the side window removed" style="background:linear-gradient(150deg,#b7bcc2,#3e3a36)"></div>
    <div class="box"><svg width="24" height="16" viewBox="0 0 24 16" fill="none" stroke="#2b7bbd" stroke-width="1"><path d="M6 14V6l5-4h8v12z M6 8h13"/></svg><div class="h">Side Window Replacment</div></div>
  </div>
  <div class="svc" style="left:205px;top:1027px">
    <div class="photo" role="img" aria-label="Shattered car door window" style="background:linear-gradient(150deg,#c5d2dc,#3f5d78)"></div>
    <div class="box"><svg width="24" height="16" viewBox="0 0 24 16" fill="none" stroke="#2b7bbd" stroke-width="1"><path d="M3 14l6-11h12v11z"/><path d="M11 10l4-4M14 11l3-3"/></svg><div class="h">Car Window Replacment</div></div>
  </div>
  <div class="svc" style="left:325px;top:1027px">
    <div class="photo" role="img" aria-label="Hand adjusting a power car window" style="background:linear-gradient(150deg,#6d8a5e,#1e2a36)"></div>
    <div class="box"><svg width="24" height="16" viewBox="0 0 24 16" fill="none" stroke="#2b7bbd" stroke-width="1"><path d="M3 14l5-11h13v11z"/><path d="M12 7h5l-1.5-1.5M17 10h-5l1.5 1.5"/></svg><div class="h">Power Window Repair</div></div>
  </div>

  <div style="left:95px;top:1235px;width:150px;height:175px;background:#e6ebf0;clip-path:polygon(8% 4%,96% 0,100% 100%,0 100%)"></div>
  <div style="left:101px;top:1240px;width:138px;height:160px;background:var(--blue);clip-path:polygon(8% 4%,96% 0,100% 100%,0 100%)"></div>
  <div role="img" aria-label="Smiling customer with arms crossed" style="left:106px;top:1213px;width:146px;height:186px;background:linear-gradient(180deg,rgba(120,150,190,0) 0%,#8ea6c2 35%,#5f7fa3 100%);clip-path:polygon(35% 0,65% 0,72% 20%,100% 40%,100% 100%,0 100%,0 40%,28% 20%)"></div>
  <div class="label" style="left:269px;top:1244px">Customer reviews</div>
  <h2 class="h" style="left:269px;top:1255px;width:170px;font-size:15.5px">What Our Clients Say<br>About Us</h2>
  <div class="rule" style="left:269px;top:1296px"></div>
  <div style="left:258px;top:1296px;font-family:Oswald,sans-serif;font-size:28px;color:#c9d9ea">“</div>
  <p style="left:269px;top:1303px;width:150px;font-size:4.6px;line-height:1.8;font-style:italic;color:var(--ink)">“Lorem ipsum dolor sit amet, consectetur adipiscing elit, sed do eiusmod tempor incididunt ut labore et dolore magna aliqua. Ut enim ad minim veniam, quis nostrud exercitation.”</p>
  <p class="p" style="left:269px;top:1332px;width:150px">Duis aute irure dolor in reprehenderit in voluptate velit esse cil dolore eu fugiat nulla pariatur. Excepteur sint ocaecat cupidat at non proident, sunt in culpa qui officia deserunt.</p>
  <div style="left:368px;top:1335px;font-family:Oswald,sans-serif;font-size:28px;color:#c9d9ea">”</div>
  <div role="img" aria-label="Reviewer portrait" style="left:269px;top:1366px;width:18px;height:18px;border-radius:50%;background:linear-gradient(160deg,#9fb6cc,#2b7bbd)"></div>
  <div class="h" style="left:294px;top:1368px;font-size:5.5px;white-space:nowrap">Jordan Vale</div>
  <div style="left:294px;top:1376px;font-size:3.8px;color:var(--blue);white-space:nowrap">CEO &amp; FOUNDER</div>

  <section style="left:1px;top:1437px;width:518px;height:291px;background:var(--soft)">
    <div class="label" style="left:0;width:518px;text-align:center;top:28px">Latest updates</div>
    <h2 class="h" style="left:0;width:518px;text-align:center;top:38px;font-size:15.5px">Our News Articles &amp; Tipes</h2>
  </section>
  <div class="news" style="left:85px;top:1517px">
    <div class="photo" role="img" aria-label="Man cleaning a car window" style="background:linear-gradient(150deg,#7fa58f,#c69a3d 60%,#45634f)"></div>
    <div class="date">05<small>NOV</small></div>
    <div class="h">Lorem Ipsum Dolor Sit<br>Amet, Consectetur</div>
    <p class="p">Duis aute irure dolor in reprehenderit in voluptate velit esse cil dolore.</p>
  </div>
  <div class="news" style="left:205px;top:1517px">
    <div class="photo" role="img" aria-label="Driver looking through a smashed windshield" style="background:linear-gradient(150deg,#c9d8e4,#5f7f9c)"></div>
    <div class="date">08<small>DEC</small></div>
    <div class="h">Sed Do Eiusmod Tempor<br>Incididunt Ut</div>
    <p class="p">Duis aute irure dolor in reprehenderit in voluptate velit esse cil dolore.</p>
  </div>
  <div class="news" style="left:325px;top:1517px">
    <div class="photo" role="img" aria-label="Damaged car windshield up close" style="background:linear-gradient(150deg,#b8c2cc,#2d3642)"></div>
    <div class="date">13<small>JAN</small></div>
    <div class="h">Enim Ad Minim Veniam<br>Quis Nostrud</div>
    <p class="p">Duis aute irure dolor in reprehenderit in voluptate velit esse cil dolore.</p>
  </div>

  <footer class="foot" style="left:1px;top:1728px;width:518px;height:204px;background:var(--black)">
    <div style="left:87px;top:88px;width:18px;height:30px;background:var(--blue)"></div>
    <div class="logo" style="left:110px;top:96px;font-size:10px">HARBORLINE</div>
    <div class="logo" style="left:110px;top:109px;font-size:4px;letter-spacing:1.6px;color:#fff">AUTO GLASS</div>
    <div style="left:93px;top:128px;width:10px;height:10px;border-radius:50%;background:var(--blue)"></div>
    <div style="left:109px;top:128px;width:10px;height:10px;border-radius:50%;background:var(--blue)"></div>
    <div style="left:125px;top:128px;width:10px;height:10px;border-radius:50%;background:var(--blue)"></div>
    <div style="left:141px;top:128px;width:10px;height:10px;border-radius:50%;background:var(--blue)"></div>

    <h4 style="left:218px;top:77px">Quick Links</h4>
    <div class="rule" style="left:218px;top:89px;width:18px"></div>
    <ul class="links-quick">
      <li style="left:218px;top:96px">Home</li>
      <li style="left:218px;top:108px">Services</li>
      <li style="left:218px;top:121px">About Us</li>
      <li style="left:218px;top:133px">Locations</li>
      <li style="left:218px;top:146px">Contact Us</li>
    </ul>

    <h4 style="left:291px;top:77px">Our Services</h4>
    <div class="rule" style="left:291px;top:89px;width:18px"></div>
    <ul class="links-services">
      <li style="left:291px;top:96px">Windshield Repair</li>
      <li style="left:291px;top:108px">Windshield Replacment Rear</li>
      <li style="left:291px;top:121px">Windshield Replacment</li>
      <li style="left:291px;top:133px">Side Window Replacment</li>
      <li style="left:291px;top:146px">Car Window Replacment</li>
    </ul>

    <h4 style="left:385px;top:77px">Why Harborline</h4>
    <div class="rule" style="left:385px;top:89px;width:18px"></div>
    <ul class="links-why">
      <li style="left:385px;top:96px">Mobile And In-Shop</li>
      <li style="left:385px;top:108px">Customer Reviews</li>
      <li style="left:385px;top:121px">Glass Recycling</li>
      <li style="left:385px;top:133px">Nationwide Warranty</li>
      <li style="left:385px;top:146px">Why Choose Harborline</li>
    </ul>

    <div style="left:84px;top:180px;width:351px;height:1px;background:#2a2a2a"></div>
    <div class="small" style="left:84px;top:189px">Copyright © 2022 HARBORLINE AUTO GLASS. All Right Reserved</div>
    <div class="small" style="left:366px;top:189px">Terms Of Use &nbsp;|&nbsp; Privacy Policy</div>
  </footer>

  <div style="left:86px;top:1692px;width:349px;height:84px;background:linear-gradient(90deg,#1f5f96,#2b7bbd);clip-path:polygon(4% 0,96% 0,100% 22%,100% 100%,0 100%,3% 70%)">
    <div class="label" style="left:39px;top:19px;color:#fff">Contact with us</div>
    <div class="h" style="left:39px;top:30px;width:200px;font-size:14.5px;color:#fff;line-height:1.2">Need Any Help For Auto<br>Repair Services</div>
    <div class="btn" style="left:252px;top:40px;background:#fff;color:var(--blue);padding:0 12px">Learn More »</div>
  </div>

</div>
</div>
</body>
</html>
```